New Advertising Company Business Card

A two sided business card. One side with logo only and the other side with my information and maybe my logo again. Looking for something unique and creative, but not too busy. Info would include my name(Marcus Fenley), President, phone number, address, email address, and website. LOGO IS THE BLUE AND WHITE ONE.

Target Market(s)

CEO/VP Level Audience

Industry/Entity Type

Business

Contact Information for Business Card

In Description.

```html
<!DOCTYPE html>
<html lang="en">
<head>
<meta charset="utf-8">
<title>Harborline Advertising – Business Card</title>
<link href="https://fonts.googleapis.com/css2?family=Montserrat:wght@500;600&family=Open+Sans:wght@400;700&display=swap" rel="stylesheet">
<style>
  :root {
    --backdrop: #ececec;
    --paper: #ffffff;
    --brand-blue: #0a6fbd;
    --brand-blue-deep: #0b4f97;
    --brand-blue-light: #1b7fd0;
    --ink: #111111;
    --text: #222222;
    --white: #ffffff;
  }
  * { margin: 0; padding: 0; box-sizing: border-box; }
  html, body { width: 1200px; height: 960px; overflow: hidden; }
  body {
    background: var(--backdrop);
    position: relative;
    font-family: "Open Sans", Arial, sans-serif;
  }
  .card {
    position: absolute;
    overflow: hidden;
    box-shadow: 0 3px 8px rgba(0,0,0,0.25);
  }
  .card-front { left: 265px; top: 70px; width: 675px; height: 385px; background: var(--paper); }
  .card-back  { left: 265px; top: 507px; width: 672px; height: 385px; background: var(--brand-blue); }

  .wave { position: absolute; left: 0; top: 0; width: 675px; height: 385px; }

  .brand-name {
    position: absolute;
    font-family: "Montserrat", Arial, sans-serif;
    font-weight: 600;
    text-align: center;
    line-height: 1;
  }
  .brand-name .brand-main { display: block; letter-spacing: 3px; }
  .brand-name .brand-sub { display: block; letter-spacing: 6px; margin-top: 8px; }

  .card-front .brand-name { left: 38px; top: 108px; width: 260px; color: var(--ink); }
  .card-front .brand-main { font-size: 38px; }
  .card-front .brand-sub { font-size: 19px; }

  .address {
    position: absolute; left: 364px; top: 143px;
    font-size: 18px; line-height: 26px; color: var(--text);
  }
  .contact-list { position: absolute; left: 364px; top: 204px; list-style: none; }
  .contact-list li {
    display: flex; align-items: center; height: 27px;
    font-size: 18px; color: var(--text);
  }
  .contact-icon { width: 22px; height: 22px; margin-right: 12px; flex: none; }

  .holder {
    position: absolute; left: 67px; top: 303px; width: 200px;
    text-align: center;
  }
  .holder-name { font-weight: 700; font-size: 20px; color: var(--white); letter-spacing: 0.2px; }
  .holder-title { font-size: 16px; color: var(--brand-blue-light); margin-top: 2px; }

  .world-map {
    position: absolute; left: 20px; top: 30px; width: 640px; height: 325px;
    background: radial-gradient(ellipse at center, rgba(255,255,255,0.10), rgba(255,255,255,0.03) 70%, rgba(255,255,255,0) 100%);
  }
  .card-back .brand-name { left: 136px; top: 190px; width: 400px; color: var(--white); }
  .card-back .brand-main { font-size: 48px; }
  .card-back .brand-sub { font-size: 22px; margin-top: 10px; }

  .back-web {
    position: absolute; left: 0; right: 0; top: 343px;
    display: flex; align-items: center; justify-content: center; gap: 14px;
    font-size: 15px; color: var(--white);
  }
  .rule { width: 125px; height: 2px; background: linear-gradient(90deg, rgba(255,255,255,0), var(--white)); }
  .rule-right { background: linear-gradient(90deg, var(--white), rgba(255,255,255,0)); }
</style>
</head>
<body>

<section class="card card-front">
  <svg class="wave" viewBox="0 0 675 385" aria-hidden="true">
    <path fill="var(--brand-blue)" d="M0,255 C140,205 280,222 420,288 S610,332 675,278 L675,385 L0,385Z"/>
    <path fill="var(--brand-blue-deep)" d="M0,275 C140,220 272,234 412,298 S602,348 675,312 L675,385 L0,385Z"/>
    <path fill="var(--ink)" d="M0,300 C130,230 262,242 402,306 S598,372 675,345 L675,385 L0,385Z"/>
  </svg>

  <div class="brand-name">
    <span class="brand-main">HARBORLINE</span>
    <span class="brand-sub">ADVERTISING</span>
  </div>

  <address class="address" style="font-style:normal">4820 Marlow St,<br>Austin, TX 78704</address>

  <ul class="contact-list">
    <li>
      <svg class="contact-icon" viewBox="0 0 22 22" aria-hidden="true">
        <circle cx="11" cy="11" r="11" fill="var(--brand-blue)"/>
        <path fill="#fff" d="M7.2,5.5 l2,-0.3 1.2,3 -1.3,1 c0.6,1.4 1.6,2.4 3,3 l1,-1.3 3,1.2 -0.3,2 c-4.8,0.4 -9,-3.8 -8.6,-8.6z"/>
      </svg>
      512 555 0148
    </li>
    <li>
      <svg class="contact-icon" viewBox="0 0 22 22" aria-hidden="true">
        <circle cx="11" cy="11" r="11" fill="var(--brand-blue)"/>
        <rect x="5" y="7" width="12" height="8.5" fill="none" stroke="#fff" stroke-width="1.5"/>
        <path d="M5,7 L11,12 L17,7" fill="none" stroke="#fff" stroke-width="1.5"/>
      </svg>
      info@harborlineads.com
    </li>
    <li>
      <svg class="contact-icon" viewBox="0 0 22 22" aria-hidden="true">
        <circle cx="11" cy="11" r="11" fill="var(--brand-blue)"/>
        <g fill="none" stroke="#fff" stroke-width="1.2">
          <circle cx="11" cy="11" r="6.5"/>
          <ellipse cx="11" cy="11" rx="3" ry="6.5"/>
          <line x1="4.5" y1="11" x2="17.5" y2="11"/>
          <line x1="11" y1="4.5" x2="11" y2="17.5"/>
        </g>
      </svg>
      www.harborlineads.com
    </li>
  </ul>

  <div class="holder">
    <p class="holder-name">MARCUS FENLEY</p>
    <p class="holder-title">President</p>
  </div>
</section>

<section class="card card-back">
  <div class="world-map" role="img" aria-label="Faint dotted world map in a lighter blue"></div>

  <div class="brand-name">
    <span class="brand-main">HARBORLINE</span>
    <span class="brand-sub">ADVERTISING</span>
  </div>

  <div class="back-web">
    <span class="rule"></span>
    <span>www.harborlineads.com</span>
    <span class="rule rule-right"></span>
  </div>
</section>

</body>
</html>
```